Brill Insurance Agency - Business Cards

Hello, I am needing new trendy business cards for our Insurance Agency now that I have a new Logo. I have attached our new logo with several color options along with a business card design that I like. I am leaning towards burgundy and blue colors. I have attached our current business card. I have also attached a headshot of our company president, Martin Vale, that you can use if you wish. Thank you so much in advance for all the wonderful designs!!!!

Target Market(s)

We want to look very professional to potential customers and we also want to look very professional so insurance companies will want to contract with us to sell their product.

Industry/Entity Type

Insurance

Contact Information for Business Card

Martin Vale
mvale@brillagency.com
Business: 555-213-4087
Fax: 555-213-7751
Cell: 555-390-2618
Toll Free: 888-555-0194
42 W Elm Rd Butler, MO 64730
www.brillagency.net

Font styles to use
Serif
Sans Serif

Colors
0355a3
3277b5
f04a50
ec1f27

Requirements
Nice to have
• I love creativity. The more creative and balanced a business card design the more I will like it. I would like the card to be printed horizontally instead of vertically.
Should not have
• My project should not have the Allied Coverage Network logo. It is no longer used in the industry.

```html
<!DOCTYPE html>
<html lang="en">
<head>
<meta charset="utf-8">
<title>Brill Insurance Agency – Business Cards</title>
<link href="https://fonts.googleapis.com/css2?family=Open+Sans:wght@400;600;700&display=swap" rel="stylesheet">
<style>
  :root {
    --blue: #0355a3;
    --blue-light: #3277b5;
    --red: #ec1f27;
    --red-soft: #f04a50;
    --white: #ffffff;
    --ink: #3a3a3a;
    --backdrop: #2e3033;
  }
  * { box-sizing: border-box; margin: 0; padding: 0; }
  html, body { width: 1200px; height: 1000px; overflow: hidden; }
  body {
    background: var(--backdrop);
    font-family: "Open Sans", Arial, sans-serif;
    position: relative;
  }
  .card {
    position: absolute;
    left: 270px;
    width: 660px;
    height: 375px;
    border-radius: 24px;
    overflow: hidden;
  }
  /* back side */
  .card-back { top: 70px; background: var(--blue); }
  .badge { position: absolute; background: var(--blue-light); }
  .badge-left { left: 30px; top: 30px; width: 80px; height: 46px; border-radius: 6px; }
  .badge-right { right: 30px; top: 26px; width: 54px; height: 54px; border-radius: 50%; }
  .back-mark {
    position: absolute; left: 0; right: 0; top: 130px;
    display: flex; align-items: center; justify-content: center; gap: 20px;
  }
  .back-mark .dot {
    width: 84px; height: 84px; border-radius: 50%;
    border: 10px solid var(--white);
  }
  .back-mark .name {
    color: var(--white); font-weight: 700; font-size: 34px; letter-spacing: 1px;
    text-transform: uppercase;
  }
  .website {
    position: absolute; right: 40px; bottom: 26px;
    color: var(--white); font-size: 19px; letter-spacing: 4px;
  }
  /* front side */
  .card-front { top: 530px; background: var(--white); }
  .front-brand {
    position: absolute; left: 0; right: 0; top: 50px;
    display: flex; align-items: center; justify-content: center; gap: 18px;
  }
  .front-brand .dot {
    width: 56px; height: 56px; border-radius: 50%; background: var(--red);
  }
  .front-brand .rule { width: 1px; height: 72px; background: var(--ink); }
  .front-brand .name {
    color: var(--blue); font-weight: 700; font-size: 25px; line-height: 1.2;
    text-transform: uppercase; letter-spacing: 0.5px;
  }
  .band {
    position: absolute; left: 0; right: 0; bottom: 0; height: 180px;
    background: var(--blue); color: var(--white);
    border-top: 5px solid var(--red-soft);
    display: flex; align-items: center;
  }
  .person {
    width: 315px; padding-right: 26px; text-align: right;
  }
  .person .full-name { font-weight: 700; font-size: 27px; letter-spacing: 0.5px; line-height: 1.2; }
  .person .role { font-size: 18px; margin-bottom: 6px; }
  .person .address { font-size: 17px; line-height: 1.35; }
  .band .divider { width: 1px; height: 124px; background: var(--white); }
  .contacts { list-style: none; padding-left: 26px; font-size: 18px; line-height: 1.5; }
  .contacts li { display: flex; align-items: center; gap: 10px; }
  .contacts svg { width: 17px; height: 17px; fill: var(--white); flex: none; }
</style>
</head>
<body>
  <section class="card card-back" aria-label="Card back">
    <div class="badge badge-left" aria-hidden="true"></div>
    <div class="badge badge-right" aria-hidden="true"></div>
    <div class="back-mark">
      <span class="dot"></span>
      <span class="name">Brill Insurance</span>
    </div>
    <p class="website">www.brillagency.net</p>
  </section>

  <section class="card card-front" aria-label="Card front">
    <div class="front-brand">
      <span class="dot"></span>
      <span class="rule"></span>
      <span class="name">Brill Insurance<br>Agency Inc</span>
    </div>
    <div class="band">
      <div class="person">
        <p class="full-name">MARTIN VALE</p>
        <p class="role">PRESIDENT</p>
        <p class="address">42 W Elm Rd P.O.Box 220<br>Butler, MO 64730</p>
      </div>
      <span class="divider"></span>
      <ul class="contacts">
        <li><svg viewBox="0 0 16 16"><path d="M3 2h3l1.5 3.5-2 1.2a8 8 0 0 0 3.8 3.8l1.2-2L14 10v3a1 1 0 0 1-1 1A11 11 0 0 1 2 3a1 1 0 0 1 1-1z"/></svg>555-213-4087, ext.23</li>
        <li><svg viewBox="0 0 16 16"><path d="M5 1h6a1 1 0 0 1 1 1v12a1 1 0 0 1-1 1H5a1 1 0 0 1-1-1V2a1 1 0 0 1 1-1zm0 2v9h6V3zm3 10a.8.8 0 1 0 0 1.6A.8.8 0 0 0 8 13z"/></svg>888-555-0194 (TF)</li>
        <li><svg viewBox="0 0 16 16"><path d="M4 1h6l2 2v3H4zM2 7h12a1 1 0 0 1 1 1v5a1 1 0 0 1-1 1H2a1 1 0 0 1-1-1V8a1 1 0 0 1 1-1zm2 2v2h8V9z"/></svg>555-213-7751</li>
        <li><svg viewBox="0 0 16 16"><path d="M1 3h14v10H1zm1.5 1.5L8 9l5.5-4.5z"/></svg>mvale@brillagency.com</li>
      </ul>
    </div>
  </section>
</body>
</html>
```